Design Guideline for an Overview Graphic
Title: Circular Economy & Future Business Models
Objective: Summarize key innovation fields, business models, and sustainability opportunities for Voltara AG in the circular economy.

1. Structure & Layout
A. Circular Economy Principles (Top Section / Centerpiece)
Goal: Introduce the fundamentals of circular economy in a visually engaging way.
πŸ”Ή Reduce β†’ Minimize resource usage
πŸ”Ή Reuse β†’ Extend product lifecycles
πŸ”Ή Recycle β†’ Reintegrate materials into production
πŸ–ŒοΈ Design Suggestion:
β€’ A circular flowchart with three interconnected icons (one for each principle).
β€’ Arrows connecting them to show the cyclical nature.

B. Key Innovation Fields (Main Body – 5 Thematic Blocks)
Each block represents a strategic business opportunity in the circular economy.

1st Circular Material Use in Waste & Water Management
πŸ“Œ Key Innovations:
βœ… Urban Mining (Extracting raw materials from waste)
β€’ Example: Brasken Recycling
βœ… Water Recycling & Reuse
β€’ Industrial wastewater treatment
β€’ Example: Quendra Water Technologies
βœ… Biomass for Energy Generation
β€’ Organic waste to biofuel
β€’ Example: Haldrup biogas plant
β€’ Icons for waste, water, and biomass
β€’ Infographic-style arrows connecting waste to usable resources

2. Circular Energy Use & Storage Technologies
πŸ“Œ Key Innovations:
βœ… Second-Life Batteries
β€’ EV batteries reused as stationary storage
β€’ Example: Toralo pCell
βœ… Hydrogen Economy
β€’ Power-to-gas technology
β€’ Example: Gasvia Transit Germany
βœ… Industrial Waste Heat Recovery
β€’ Reusing waste heat for energy
β€’ Example: Q. RX Waste Heat Recovery
β€’ Battery, hydrogen, and heat recovery icons
β€’ Use energy flow arrows to show repurposing

3. As-a-Service Models for Sustainability
πŸ“Œ Key Innovations:
βœ… Heat-as-a-Service (Leased heating solutions)
β€’ Example: Lindquast WΓ€rme
βœ… Water as a Service (Industrial water management)
β€’ Example: Ombra
βœ… Zero-waste logistics for companies
β€’ Material return & reuse services
β€’ Example: Swirl by GaiaBin
β€’ Modular grid design with icons & short descriptions
β€’ Flowchart representation of the service process

4th ICT & AI for Circular Economy
πŸ“Œ Key Innovations:
βœ… Digital Platforms for Resource Sharing
β€’ Example: Polvano (Plastics Marketplace)
βœ… AI-Based Waste Sorting
β€’ Machine learning-driven waste classification
β€’ Example: KEV Robotics
βœ… IoT for Water Management
β€’ Real-time leak detection
β€’ Example: Moravec Dynamics Water Management
β€’ Icons for AI, IoT, and digital platforms
β€’ Tech-style visualization (data points, connections, automation lines)

```html
<!DOCTYPE html>
<html lang="en">
<head>
<meta charset="utf-8">
<title>Circular Economy &amp; Future Business Models</title>
<link href="https://fonts.googleapis.com/css2?family=Lato:wght@400;700&display=swap" rel="stylesheet">
<style>
:root{
  --bg:#9a9e9f;
  --lime:#8aad00;
  --olive:#4f6a00;
  --ink:#3b3b3b;
  --ink-soft:#4a4a4a;
  --white:#ffffff;
  --tan:#d9bf9a;
  --tan-deep:#c8ab82;
  --teal:#00a85a;
  --teal-deep:#0a8f4e;
  --blue:#1f8fd6;
  --navy:#1d2b45;
}
*{margin:0;padding:0;box-sizing:border-box}
html,body{width:1200px;height:796px;overflow:hidden}
body{background:var(--bg);font-family:"Lato",sans-serif;color:var(--ink);position:relative}
.page{position:absolute;width:228px;height:322px;background:var(--white);box-shadow:2px 3px 6px rgba(0,0,0,.25);overflow:hidden}
.line{position:absolute;white-space:nowrap;line-height:1.15}

/* header band */
.band-wrap{position:absolute}
.band-wrap .fill{position:absolute;left:0;top:0;bottom:0;background:var(--lime);
  clip-path:polygon(0 0,100% 0,calc(100% - 9px) 100%,0 100%);color:var(--white);
  display:flex;align-items:center;padding-left:9px;font-size:12.5px;line-height:1.2}
.band-wrap .slash{position:absolute;top:0;bottom:0;width:6px;background:var(--olive);transform:skewX(22deg);transform-origin:top}

/* footer */
.foot{position:absolute;left:96px;width:124px;height:11px;background:var(--lime);
  clip-path:polygon(14px 0,100% 0,100% 100%,0 100%);color:var(--white);font-size:4.6px;
  display:flex;align-items:center;justify-content:center;padding-left:14px}
.foot::before{content:"";position:absolute;left:0;top:0;width:22px;height:11px;background:var(--olive);
  clip-path:polygon(14px 0,22px 0,8px 100%,0 100%)}

/* cover */
.cover{background:var(--lime)}
.cover-title{position:absolute;top:52px;left:0;width:100%;text-align:center;color:var(--white);
  font-weight:700;font-variant:small-caps;font-size:21px;line-height:25px}
.cover-photo{position:absolute;left:0;top:120px;width:100%;height:204px;
  background:radial-gradient(circle at 40% 45%,#b9d63a 0%,#7fa51a 35%,#5b7d12 60%,#2f4a10 100%)}

/* objective */
.objective-title{position:absolute;left:18px;top:70px;font-size:22px;line-height:26px;font-weight:400;color:var(--olive)}
.diamond{position:absolute;width:14px;height:14px;background:var(--olive);transform:rotate(45deg)}
.obj-text{position:absolute;left:61px;font-size:11px;line-height:13px;color:var(--ink)}

/* text styles */
.h-main{font-size:12.5px;color:var(--ink)}
.h-sub{font-size:10px;color:var(--ink-soft)}
.t-bullet{font-size:7.2px;color:var(--ink)}
.t-note{font-size:5px;color:var(--ink)}

/* back */
.back{background:linear-gradient(160deg,#94bd12 0%,#88b40a 50%,#7fb21c 100%)}
.back-art{position:absolute;inset:0;background:radial-gradient(circle at 55% 55%,rgba(255,255,255,.08) 0%,rgba(255,255,255,0) 60%)}
.contact{position:absolute;left:0;width:100%;text-align:center;color:var(--white);font-size:11px;line-height:13px}
</style>
</head>
<body>

<!-- Cover -->
<section class="page cover" style="left:62px;top:45px;width:232px;height:324px">
  <h1 class="cover-title">Circular Economy &amp;<br>Future Business Models</h1>
  <div class="cover-photo" role="img" aria-label="Photo of a businessman touching a glowing green recycling symbol in a sunny field"></div>
</section>

<!-- Objective -->
<section class="page" style="left:341px;top:40px">
  <div class="band-wrap" style="left:6px;top:20px;width:200px;height:36px">
    <div class="fill" style="width:186px">Circular Economy &amp;<br>Future Business Models</div>
    <div class="slash" style="left:178px"></div>
  </div>
  <h2 class="objective-title">Objective</h2>
  <div class="diamond" style="left:37px;top:117px"></div>
  <p class="obj-text" style="top:114px">Summarize key innovation<br>fields</p>
  <div class="diamond" style="left:37px;top:153px"></div>
  <p class="obj-text" style="top:154px">Business models</p>
  <div class="diamond" style="left:37px;top:182px"></div>
  <p class="obj-text" style="top:182px;left:59px">Sustainability opportunities<br>for Voltara AG in the circular<br>economy</p>
  <div class="foot" style="top:307px">555 014 2871 | www.circulink.com</div>
</section>

<!-- Structure & Layout -->
<section class="page" style="left:618px;top:47px">
  <div class="band-wrap" style="left:24px;top:13px;width:140px;height:26px">
    <div class="fill" style="width:130px">Structure &amp; Layout</div>
    <div class="slash" style="left:124px"></div>
  </div>
  <p class="line" style="left:0;width:100%;text-align:center;top:46px;font-size:12.5px;color:var(--olive)">Circular Economy Principles</p>
  <p class="line" style="left:24px;top:70px;font-size:8.4px;color:var(--ink-soft);white-space:normal;width:196px;line-height:11px"><span style="font-size:12.5px">Goal:</span> Introduce the fundamentals of circular economy in a visually engaging way.</p>
  <svg width="228" height="322" viewBox="0 0 228 322" style="position:absolute;left:0;top:0" role="img" aria-label="Circular flow of Reduce, Recycle and Reuse around the circular economy">
    <circle cx="110" cy="156" r="42" fill="var(--tan-deep)"/>
    <circle cx="110" cy="156" r="37" fill="var(--tan)"/>
    <circle cx="61" cy="238" r="42" fill="var(--teal)"/>
    <circle cx="61" cy="238" r="36" fill="var(--teal-deep)"/>
    <circle cx="159" cy="238" r="42" fill="var(--teal)"/>
    <circle cx="159" cy="238" r="36" fill="var(--teal-deep)"/>
    <circle cx="110" cy="210" r="32" fill="var(--white)"/>
    <circle cx="110" cy="210" r="28" fill="var(--blue)"/>
    <circle cx="110" cy="137" r="9" fill="none" stroke="var(--navy)" stroke-width="4" stroke-dasharray="3 2"/>
    <circle cx="110" cy="137" r="6" fill="none" stroke="var(--navy)" stroke-width="3"/>
    <rect x="55" y="220" width="12" height="14" rx="1.5" fill="var(--navy)"/>
    <rect x="53" y="217" width="16" height="3" fill="var(--navy)"/>
    <circle cx="61" cy="227" r="2.5" fill="none" stroke="var(--white)" stroke-width="1"/>
    <g transform="rotate(-18 160 221)">
      <rect x="149" y="215" width="22" height="12" rx="1.5" fill="var(--navy)"/>
      <rect x="151" y="217" width="18" height="8" fill="none" stroke="var(--white)" stroke-width=".8"/>
      <circle cx="160" cy="221" r="2.4" fill="none" stroke="var(--white)" stroke-width=".8"/>
    </g>
    <g font-family="Lato, sans-serif" text-anchor="middle" fill="var(--white)">
      <text x="111" y="160" font-size="8.5" font-weight="700">Reduce</text>
      <text x="110" y="167" font-size="4.6">Minimize resource</text>
      <text x="110" y="172.5" font-size="4.6">usage</text>
      <text x="110" y="206" font-size="4.4" font-weight="700">CIRCULAR</text>
      <text x="110" y="214" font-size="7.6" font-weight="700">ECONOMY</text>
      <text x="62" y="246" font-size="8.5" font-weight="700">Recycle</text>
      <text x="62" y="254" font-size="4.6">Reintegrate materials</text>
      <text x="62" y="259.5" font-size="4.6">into production</text>
      <text x="160" y="245" font-size="8.5" font-weight="700">Reuse</text>
      <text x="160" y="254" font-size="4.6">Extend product</text>
      <text x="160" y="259.5" font-size="4.6">lifecycles</text>
    </g>
  </svg>
  <div class="foot" style="top:305px;left:98px">555 014 2871 | www.circulink.com</div>
</section>

<!-- Key Innovation Fields -->
<section class="page" style="left:900px;top:45px">
  <div class="band-wrap" style="left:13px;top:14px;width:146px;height:26px">
    <div class="fill" style="width:134px;padding-left:5px">Key Innovation Fields</div>
    <div class="slash" style="left:128px"></div>
  </div>
  <p class="line t-note" style="left:24px;top:68px;font-size:5.6px">Each block represents a strategic business opportunity in the</p>
  <p class="line t-note" style="left:24px;top:76px;font-size:5.6px">circular economy.</p>
  <p class="line h-main" style="left:25px;top:96px">Circular Material Use in Waste &amp;</p>
  <p class="line h-main" style="left:25px;top:111px">Water Management</p>
  <p class="line h-sub" style="left:27px;top:134px">Urban Mining <span class="t-note" style="font-size:5.4px">&nbsp;(Extracting raw materials from waste)</span></p>
  <p class="line t-bullet" style="left:41px;top:151px">Example: Brasken Recycling</p>
  <p class="line h-sub" style="left:27px;top:163px">Water Recycling &amp; Reuse</p>
  <p class="line t-bullet" style="left:42px;top:181px">&bull; Industrial wastewater treatment</p>
  <p class="line t-bullet" style="left:42px;top:190px">&bull; Example: Quendra Water Technologies</p>
  <p class="line h-sub" style="left:28px;top:204px">Biomass for Energy Generation</p>
  <p class="line t-bullet" style="left:42px;top:223px">&bull; Organic waste to biofuel</p>
  <p class="line t-bullet" style="left:42px;top:232px">&bull; Example: Haldrup biogas plant</p>
  <div class="foot" style="top:290px;left:106px;width:122px">555 014 2871 | www.circulink.com</div>
</section>

<!-- Energy & As-a-Service -->
<section class="page" style="left:72px;top:413px">
  <p class="line h-main" style="left:18px;top:21px">Circular Energy Use &amp; Storage</p>
  <p class="line h-main" style="left:18px;top:36px">Technologies</p>
  <p class="line h-sub" style="left:21px;top:58px">Second-Life Batteries</p>
  <p class="line t-bullet" style="left:36px;top:77px">&bull; EV batteries reused as stationary storage</p>
  <p class="line t-bullet" style="left:36px;top:86px">&bull; Example: Toralo pCell</p>
  <p class="line h-sub" style="left:21px;top:101px">Hydrogen Economy</p>
  <p class="line t-bullet" style="left:36px;top:119px">&bull; Power-to-gas technology</p>
  <p class="line t-bullet" style="left:36px;top:128px">&bull; Example: Gasvia Transit Germany</p>
  <p class="line h-sub" style="left:22px;top:142px">Industrial Waste Heat Recovery</p>
  <p class="line t-bullet" style="left:37px;top:161px">&bull; Reusing waste heat for energy</p>
  <p class="line t-bullet" style="left:37px;top:170px">&bull; Example: Q. RX Waste Heat Recovery</p>
  <p class="line h-main" style="left:21px;top:190px">As-a-Service Models for Sustain-</p>
  <p class="line h-main" style="left:21px;top:205px">ability</p>
  <p class="line h-sub" style="left:25px;top:226px">Heat-as-a-Service (Leased heating</p>
  <p class="line t-bullet" style="left:39px;top:243px">&bull; Example: Lindquast W&auml;rme</p>
  <p class="line h-sub" style="left:25px;top:254px">Water as a Service (Industrial water</p>
  <p class="line t-bullet" style="left:40px;top:270px">&bull; Example: Ombra</p>
  <div class="foot" style="top:296px;left:108px;width:122px">555 014 2871 | www.circulink.com</div>
</section>

<!-- Logistics & ICT -->
<section class="page" style="left:349px;top:414px">
  <p class="line" style="left:18px;top:16px;font-size:10.5px;color:var(--ink)">Zero-waste logistics for companies</p>
  <p class="line t-bullet" style="left:33px;top:35px">&bull; Material return &amp; reuse services</p>
  <p class="line t-bullet" style="left:33px;top:44px">&bull; Example: Swirl by GaiaBin</p>
  <p class="line h-main" style="left:20px;top:62px">ICT &amp; AI for Circular Economy</p>
  <p class="line h-sub" style="left:29px;top:83px">Digital Platforms for Resource Sharing</p>
  <p class="line t-bullet" style="left:44px;top:99px">&bull; Example: Polvano (Plastics Marketplace)</p>
  <p class="line h-sub" style="left:33px;top:120px">AI-Based Waste Sorting</p>
  <p class="line t-bullet" style="left:46px;top:136px">&bull; Machine learning-driven waste classification</p>
  <p class="line t-bullet" style="left:46px;top:145px">&bull; Example: KEV Robotics</p>
  <p class="line h-sub" style="left:35px;top:165px">IoT for Water Management</p>
  <p class="line t-bullet" style="left:49px;top:180px">&bull; Real-time leak detection</p>
  <p class="line t-bullet" style="left:49px;top:190px">&bull; Example: Moravec Dynamics Water Management</p>
  <div class="foot" style="top:298px;left:104px;width:122px">555 014 2871 | www.circulink.com</div>
</section>

<!-- Back cover -->
<section class="page back" style="left:620px;top:413px;width:230px;height:323px">
  <div class="back-art" role="img" aria-label="Faint green recycling-themed background image"></div>
  <p class="contact" style="top:117px">+555 014 2872<br>hello@circulink.com<br>www.circulink.com</p>
  <p class="contact" style="top:169px">14 Fernhill Road<br>country , K4 7RB</p>
</section>

</body>
</html>
```